Baby Boutique Needs a Business Card Design

We need a modern double sided business card design using the attached logo for Lil' Tot Nook.

Lil' Tot Nook is a baby boutique which sells only handmade clothing and accessories for both boys and girls. Our store will live exclusively online.

We would like to only use the colors that have been used in the logo.

Target Market(s)

Potential wholesale clients, Small business owners

Industry/Entity Type

Retail

Contact Information for Business Card

Name Wendell J. Ferris (Owner)
Email sales@ltotnook.com
Main Phone 787-203-6159
Cell phone 787-203-6742
Website www.LTotNook.com

Font styles to use
Sans Serif

Colors

Designer to choose colors to be used in the design.

Requirements
Must have
• -Would like to have icons that indentify the contact information.
• -Include our website
• -Include our tagline in a small area near the bottom. "Handmade Baby Creations"
• -Would like to include Facebook and Instagram Icons
• -
Nice to have
• Would like to have a simple back side with the logo.
• Something along the lines of the harbor ledger card attached.

```html
<!DOCTYPE html>
<html lang="en">
<head>
<meta charset="utf-8">
<title>Lil' Tot Nook — Business Card</title>
<link rel="stylesheet" href="https://fonts.googleapis.com/css2?family=Open+Sans:wght@400;600&family=Ubuntu:wght@400;500&display=swap">
<style>
  :root {
    --coral: #d95b5b;
    --teal: #7cc6b6;
    --teal-dark: #5aa596;
    --white: #ffffff;
    --ink: #333333;
    --stage: #cccccc;
    --shadow: rgba(0,0,0,0.55);
  }
  * { margin: 0; padding: 0; box-sizing: border-box; }
  html, body { width: 1120px; height: 1200px; overflow: hidden; background: var(--stage); }
  .stage { position: absolute; left: 0; top: 0; width: 1310px; height: 1404px; transform: scale(0.855); transform-origin: 0 0; }
  .card { position: absolute; left: 190px; width: 926px; box-shadow: 6px 6px 6px var(--shadow); overflow: hidden; }

  /* Front */
  .card-front { top: 28px; height: 656px; background: var(--coral); }
  .front-panel { position: absolute; left: 55px; top: 2px; width: 553px; height: 651px; background: var(--white); }
  .rule { position: absolute; top: 0; bottom: 0; width: 2px; background: var(--coral); }
  .rule-a { left: 48px; } .rule-b { left: 53px; background: var(--white); width: 2px; }
  .logo-frame { position: absolute; left: 151px; top: 23px; width: 328px; height: 237px; border: 1px solid var(--coral); }
  .logo-frame::before { content: ""; position: absolute; inset: 4px; border: 2px solid var(--coral); }
  .logo-frame::after { content: ""; position: absolute; inset: 8px; border: 1px solid var(--teal); }
  .brand-mark { position: absolute; inset: 0; display: flex; align-items: center; justify-content: center; gap: 12px; font-family: "Ubuntu", sans-serif; font-weight: 500; font-size: 40px; color: var(--teal); }
  .brand-dot { width: 16px; height: 16px; border-radius: 50%; background: var(--coral); }

  .contact-list { position: absolute; left: 22px; top: 381px; list-style: none; }
  .contact-item { display: flex; align-items: center; height: 65px; }
  .contact-icon { width: 54px; height: 52px; flex: none; }
  .contact-text { margin-left: 22px; font-family: "Open Sans", sans-serif; font-size: 23px; color: var(--coral); }

  .name-band { position: absolute; left: 608px; top: 67px; width: 315px; height: 63px; background: var(--teal); box-shadow: 4px 4px 4px var(--shadow); display: flex; align-items: center; justify-content: center; }
  .person-name { font-family: "Ubuntu", sans-serif; font-size: 33px; color: var(--coral); }

  .social { position: absolute; left: 608px; width: 318px; top: 545px; display: flex; justify-content: center; align-items: center; gap: 10px; font-family: "Open Sans", sans-serif; font-size: 20px; color: var(--ink); }
  .social-square { width: 24px; height: 24px; background: var(--teal); }
  .tagline { position: absolute; left: 608px; width: 318px; top: 600px; text-align: center; font-family: "Open Sans", sans-serif; font-size: 20px; color: var(--ink); }

  /* Back */
  .card-back { top: 709px; height: 658px; background: linear-gradient(to bottom, var(--coral) 0%, #a29a90 55%, var(--teal) 100%); }
  .back-logo { position: absolute; left: 270px; top: 160px; width: 400px; height: 340px; display: flex; align-items: center; justify-content: center; }
  .back-brand { font-family: "Ubuntu", sans-serif; font-weight: 500; font-size: 64px; color: var(--teal); }
</style>
</head>
<body>
<div class="stage">
  <section class="card card-front">
    <div class="rule rule-a"></div>
    <div class="front-panel">
      <div class="logo-frame">
        <div class="brand-mark"><span class="brand-name">Lil' Tot Nook</span><span class="brand-dot"></span></div>
      </div>
    </div>
    <ul class="contact-list">
      <li class="contact-item">
        <svg class="contact-icon" viewBox="0 0 54 52"><defs><linearGradient id="hex" x1="0" x2="1"><stop offset="0" stop-color="#5aa596"/><stop offset="1" stop-color="#e8e8e8"/></linearGradient></defs><polygon points="14,2 40,2 52,26 40,50 14,50 2,26" fill="url(#hex)" stroke="#d95b5b" stroke-width="1.5"/><path d="M20 15 q-3 2 -1 8 q4 9 12 13 q5 2 7 -1 l-4 -4 q-2 2 -4 0 q-4 -3 -6 -7 q-1 -2 1 -3 z" fill="#111"/></svg>
        <span class="contact-text">M: 787-203-6159</span>
      </li>
      <li class="contact-item">
        <svg class="contact-icon" viewBox="0 0 54 52"><polygon points="14,2 40,2 52,26 40,50 14,50 2,26" fill="url(#hex)" stroke="#d95b5b" stroke-width="1.5"/><path d="M20 15 q-3 2 -1 8 q4 9 12 13 q5 2 7 -1 l-4 -4 q-2 2 -4 0 q-4 -3 -6 -7 q-1 -2 1 -3 z" fill="#111"/></svg>
        <span class="contact-text">M: 787-203-6742</span>
      </li>
      <li class="contact-item">
        <svg class="contact-icon" viewBox="0 0 54 52"><polygon points="14,2 40,2 52,26 40,50 14,50 2,26" fill="url(#hex)" stroke="#d95b5b" stroke-width="1.5"/><rect x="14" y="18" width="26" height="17" fill="#111"/><path d="M14 18 l13 10 l13 -10" fill="none" stroke="#ddd" stroke-width="1.5"/></svg>
        <span class="contact-text">E: sales@ltotnook.com</span>
      </li>
      <li class="contact-item">
        <svg class="contact-icon" viewBox="0 0 54 52"><polygon points="14,2 40,2 52,26 40,50 14,50 2,26" fill="url(#hex)" stroke="#d95b5b" stroke-width="1.5"/><g fill="none" stroke="#111" stroke-width="2"><circle cx="27" cy="26" r="12"/><ellipse cx="27" cy="26" rx="5" ry="12"/><line x1="15" y1="26" x2="39" y2="26"/><line x1="17" y1="20" x2="37" y2="20"/><line x1="17" y1="32" x2="37" y2="32"/></g></svg>
        <span class="contact-text">W: www.LTotNook.com</span>
      </li>
    </ul>
    <div class="name-band"><span class="person-name">Wendell J. Ferris</span></div>
    <div class="social"><span class="social-square"></span><span>@ltotnook</span></div>
    <p class="tagline">"Handmade Baby Creations"</p>
  </section>

  <section class="card card-back">
    <div class="back-logo"><span class="back-brand">Lil' Tot Nook</span></div>
  </section>
</div>
</body>
</html>
```